Bluefern Realty Letterhead

Bluefern Realty Guan
417 Corrin Tide Avenue, Ste B305
Tumon, GU. 96913

Industry/Entity Type

Real Estate

Font styles to use
Serif

Colors

Designer to choose colors to be used in the design.

```html
<!DOCTYPE html>
<html lang="en">
<head>
<meta charset="utf-8">
<title>Bluefern Realty Letterhead</title>
<link href="https://fonts.googleapis.com/css2?family=Tinos:wght@400;700&display=swap" rel="stylesheet">
<style>
  :root {
    --brand-blue: #1f8fd0;
    --sky-blue: #6fcbe8;
    --map-tint: #e1f0f9;
    --band-light: #74cdea;
    --band-deep: #0b92d2;
    --sun-orange: #f8a93a;
    --paper: #ffffff;
  }
  html, body {
    margin: 0;
    padding: 0;
    overflow: hidden;
    background: var(--paper);
  }
  .letterhead {
    position: relative;
    width: 848px;
    height: 1200px;
    overflow: hidden;
    background: var(--paper);
    font-family: "Tinos", "Times New Roman", serif;
  }
  .brand {
    position: absolute;
    left: 53px;
    top: 120px;
    width: 251px;
    display: flex;
    align-items: center;
    justify-content: center;
    gap: 10px;
  }
  .brand-dot {
    width: 18px;
    height: 18px;
    border-radius: 50%;
    background: var(--sky-blue);
  }
  .brand-name {
    font-size: 31px;
    font-weight: 400;
    color: var(--sky-blue);
    white-space: nowrap;
  }
  .rule {
    position: absolute;
    top: 184px;
    height: 1px;
    background: var(--brand-blue);
  }
  .rule-left { left: 53px; width: 251px; }
  .rule-right { left: 324px; width: 470px; }
  .sender {
    position: absolute;
    right: 54px;
    top: 106px;
    text-align: right;
    color: var(--brand-blue);
    font-size: 15px;
    line-height: 22px;
    font-style: normal;
  }
  .sender-name {
    font-weight: 700;
    font-size: 17px;
    margin-bottom: 2px;
  }
  .island-map {
    position: absolute;
    left: 209px;
    top: 300px;
    width: 434px;
    height: 630px;
    border-radius: 48% 52% 46% 54% / 40% 44% 56% 60%;
    background: radial-gradient(ellipse at center, var(--map-tint) 55%, rgba(225,240,249,0) 100%);
  }
  .footer-band {
    position: absolute;
    left: 0;
    top: 1080px;
    width: 848px;
    height: 120px;
    background: linear-gradient(90deg, var(--band-light), var(--band-deep));
  }
  .contact {
    position: absolute;
    right: 50px;
    top: 1107px;
    color: var(--paper);
    font-size: 15px;
    line-height: 22.5px;
    text-align: right;
  }
  .contact-item {
    display: flex;
    align-items: center;
    justify-content: flex-end;
    gap: 9px;
  }
  .contact-icon {
    width: 14px;
    height: 14px;
    flex: none;
  }
</style>
</head>
<body>
<main class="letterhead">
  <div class="brand">
    <span class="brand-dot"></span>
    <span class="brand-name">Bluefern Realty</span>
  </div>
  <div class="rule rule-left"></div>
  <div class="rule rule-right"></div>

  <address class="sender">
    <div class="sender-name">Bluefern Realty Guan</div>
    <div>417 Corrin Tide Avenue, Ste B305</div>
    <div>Tumon, GU. 96913</div>
  </address>

  <div class="island-map" role="img" aria-label="Faint pale blue map silhouette of the island of Guam"></div>

  <div class="footer-band" role="img" aria-label="Decorative blue ocean wave footer band"></div>

  <div class="contact">
    <div class="contact-item">
      <span>(671) 555-0147</span>
      <svg class="contact-icon" viewBox="0 0 24 24"><path d="M6.6 10.8a15.1 15.1 0 0 0 6.6 6.6l2.2-2.2a1 1 0 0 1 1-.25 11.4 11.4 0 0 0 3.6.57 1 1 0 0 1 1 1V20a1 1 0 0 1-1 1A17 17 0 0 1 3 4a1 1 0 0 1 1-1h3.5a1 1 0 0 1 1 1c0 1.25.2 2.45.57 3.57a1 1 0 0 1-.25 1Z" fill="var(--sun-orange)"/></svg>
    </div>
    <div class="contact-item">
      <span>mara@bluefernrealtyguam.com</span>
      <svg class="contact-icon" viewBox="0 0 24 24"><rect x="2" y="5" width="20" height="14" fill="var(--sun-orange)"/><path d="M2 5l10 8 10-8" fill="none" stroke="#ffffff" stroke-width="1.5"/></svg>
    </div>
    <div class="contact-item">
      <span>bluefernrealtyguam.com</span>
      <svg class="contact-icon" viewBox="0 0 24 24"><g fill="none" stroke="var(--sun-orange)" stroke-width="2"><circle cx="12" cy="12" r="10"/><ellipse cx="12" cy="12" rx="4.5" ry="10"/><path d="M2 12h20M4 7h16M4 17h16"/></g></svg>
    </div>
  </div>
</main>
</body>
</html>
```